ZEST its me again- No TIME

I am a weight loss consultant who my target audience now is staff- teachers at work.

I am Zest Wellbeing and I have partner up with the program Vital Kickoff. I am selling my services but it will be attached to his brochure which I attached to show you.

This flyer will be given to teachers while at work or left on the staff room lunch table.

Please make it short, snappy and fun.
Why lose weight at work? People are time poor

points:-
- Mobile weight loss consultant who comes to you at work
before/after school or lunch break.
-20 minute private 1 on 1 consultations
-limited spots (3 per hour)
-no contract
-10 years experience

If possible I would like it at work flyer for different companies as well like banks but teachers/schools are my main target.

Like the picture with the teacher in front of the board but can remove the heart if possible
Thank you

i will brochure soon to show you

Target Market(s)

people at work- during lunch breaks or before and after
First is school teachers then other companies.
Females are the majority of clients

Industry/Entity Type

Teacher

Requirements
Must have
• leave it up to you just want to grab staff's attention.
Should not have
• please never use the word "diet" its a healthy lifestyle.

```html
<!DOCTYPE html>
<html lang="en">
<head>
<meta charset="utf-8">
<title>Why lose weight at work? – Zest Wellbeing</title>
<link href="https://fonts.googleapis.com/css2?family=Open+Sans:wght@400;600;700;800&display=swap" rel="stylesheet">
<style>
  :root {
    --plum: #5a2d6e;
    --plum-dark: #3f1d52;
    --accent-red: #d9283a;
    --teal-band: rgba(40, 150, 180, 0.78);
    --white: #ffffff;
    --ink: #4a3a5c;
    --green: #8cc63f;
    --yellow: #f4d03f;
    --red: #e8505b;
    --blue: #4aa8d8;
  }
  * { margin: 0; padding: 0; box-sizing: border-box; }
  html, body { width: 851px; height: 1200px; overflow: hidden; background: #fff; }
  .flyer {
    position: relative; width: 851px; height: 1200px; overflow: hidden;
    font-family: "Open Sans", Arial, sans-serif; background: var(--white);
  }
  .headline-bar {
    position: absolute; top: 0; left: 0; width: 100%; height: 86px;
    background: var(--white); border-bottom: 6px solid var(--accent-red);
    display: flex; align-items: center; justify-content: center; z-index: 3;
  }
  .headline-bar h1 { color: var(--plum); font-weight: 800; font-size: 50px; letter-spacing: -0.5px; }
  .classroom-photo {
    position: absolute; top: 92px; left: 0; width: 100%; height: 1030px;
    background:
      radial-gradient(ellipse 320px 420px at 640px 420px, #d9b7a6 0%, rgba(217,183,166,0) 70%),
      linear-gradient(160deg, #1f4f6e 0%, #2f7391 35%, #6fa7b8 60%, #c9d6d6 100%);
  }
  .time-band {
    position: absolute; top: 110px; left: 110px; right: 0; height: 86px;
    background: var(--teal-band); display: flex; align-items: center; justify-content: center;
    z-index: 2;
  }
  .time-band h2 { color: var(--white); font-weight: 600; font-size: 48px; }
  .service-intro {
    position: absolute; top: 238px; left: 100px; width: 470px; z-index: 2;
    color: var(--white); font-size: 29px; line-height: 1.3;
  }
  .service-intro .lead { font-size: 42px; font-weight: 600; }
  .service-intro .role { font-weight: 700; font-size: 30px; white-space: nowrap; }
  .lower-sweep { position: absolute; left: 0; top: 560px; width: 851px; height: 570px; z-index: 1; }
  .points {
    position: absolute; top: 705px; left: 40px; list-style: none; z-index: 2;
    display: flex; flex-direction: column; align-items: flex-start; gap: 6px;
  }
  .points li {
    position: relative; font-size: 32px; font-weight: 600; color: var(--ink);
    height: 56px; line-height: 56px; padding: 0 12px 0 10px; white-space: nowrap;
  }
  .points li::before {
    content: ""; position: absolute; left: 0; right: 0; top: 12px; height: 34px;
    border-radius: 18px; opacity: 0.75; z-index: -1;
  }
  .points li.green::before { background: var(--green); }
  .points li.yellow::before { background: var(--yellow); }
  .points li.red::before { background: var(--red); }
  .points li.blue::before { background: var(--blue); }
  .brand-mark {
    position: absolute; right: 40px; top: 960px; z-index: 2;
    display: flex; align-items: center; gap: 14px;
  }
  .brand-mark .dot { width: 56px; height: 56px; border-radius: 50%; background: var(--plum); }
  .brand-mark span { font-size: 38px; font-weight: 700; color: var(--plum); }
  .fitness-items {
    position: absolute; left: 28px; top: 995px; width: 170px; height: 120px; z-index: 2;
    background: linear-gradient(135deg, #e1364a 0%, #f2f2f2 50%, #8cc63f 100%); border-radius: 8px;
  }
  .partner-badge {
    position: absolute; left: 235px; top: 1000px; width: 140px; height: 110px; z-index: 2;
    background: #eceaf0; border: 3px solid #d22b36; border-radius: 6px;
  }
  .contact-footer {
    position: absolute; bottom: 0; left: 0; width: 100%; height: 78px;
    background: var(--plum); color: var(--white); z-index: 3;
    display: flex; flex-direction: column; justify-content: center; align-items: center;
    font-size: 21px; line-height: 1.45;
  }
  .contact-footer .sep { padding: 0 12px; }
</style>
</head>
<body>
<div class="flyer">
  <header class="headline-bar"><h1>Why lose weight at work?</h1></header>

  <div class="classroom-photo" role="img" aria-label="Teacher holding an open book in front of a classroom whiteboard with students"></div>

  <div class="time-band"><h2>People are time poor</h2></div>

  <div class="service-intro">
    <p class="lead">Mobile</p>
    <p class="role">WEIGHT LOSS CONSULTANT</p>
    <p>who comes to you at work<br>before/after school<br>or lunch break.</p>
  </div>

  <svg class="lower-sweep" viewBox="0 0 851 570" preserveAspectRatio="none" aria-hidden="true">
    <path d="M0 150 C 250 60, 520 40, 851 0 L851 570 L0 570 Z" fill="#f4f2f6" opacity="0.95"/>
    <path d="M0 120 C 250 40, 520 20, 851 -20" fill="none" stroke="#ffffff" stroke-width="8" opacity="0.8"/>
  </svg>

  <ul class="points">
    <li class="green">20 minute private 1 on 1 consultations</li>
    <li class="yellow">Limited spots (3 per hour)</li>
    <li class="red">No contract</li>
    <li class="blue">10 years experience</li>
  </ul>

  <div class="brand-mark"><div class="dot"></div><span>Zest Wellbeing</span></div>

  <div class="fitness-items" role="img" aria-label="Red hand weights, an apple and a measuring tape"></div>
  <div class="partner-badge" role="img" aria-label="Partner program badge"></div>

  <footer class="contact-footer">
    <p>+61 400 123 987<span class="sep">|</span>hello@zestwellbeing.com.au</p>
    <p>www.zestwellbeing.com.au<span class="sep">|</span>Fernvale North, Victoria, Australia 3199</p>
  </footer>
</div>
</body>
</html>
```